arts & crafts

I collect old plates & make them into serving plates for cakes, afternoon teas, special occasions, weddings, parties, bridal showers. cake competitions, displays in bakeries.

Contact Information for Business Card

Tulips Turn Gold
Making vintage feel fresh again
Ph 0417283956
info@ tulipsturngold.com.au
www.tulipsturngold.com.au
pagebook
Craftlo

```html
<!DOCTYPE html>
<html lang="en">
<head>
<meta charset="utf-8">
<title>Tulips Turn Gold – Business Card</title>
<link rel="stylesheet" href="https://fonts.googleapis.com/css2?family=Fredoka:wght@600&family=Dancing+Script:wght@600&family=Arimo:wght@400;700&display=swap">
<style>
  :root {
    --backdrop: #d8d8d8;
    --card: #f0f0f0;
    --brand-blue: #1f86cf;
    --ink: #2b2b2b;
    --text: #3d3d3d;
  }
  * { box-sizing: border-box; margin: 0; padding: 0; }
  html, body {
    width: 937px;
    height: 1200px;
    overflow: hidden;
    background: var(--backdrop);
  }
  .canvas {
    position: relative;
    width: 937px;
    height: 1200px;
  }
  .business-card {
    position: absolute;
    left: 165px;
    top: 720px;
    width: 619px;
    height: 340px;
    background: var(--card);
    text-align: center;
    color: var(--text);
  }
  .brand {
    position: absolute;
    top: 118px;
    left: 0;
    right: 0;
    display: flex;
    justify-content: center;
    align-items: center;
    gap: 12px;
  }
  .brand-name {
    font-family: "Fredoka", sans-serif;
    font-weight: 600;
    font-size: 52px;
    line-height: 1;
    color: var(--brand-blue);
    white-space: nowrap;
  }
  .brand-dot {
    width: 28px;
    height: 28px;
    border-radius: 50%;
    background: var(--brand-blue);
  }
  .tagline {
    position: absolute;
    top: 180px;
    left: 0;
    right: 0;
    font-family: "Dancing Script", cursive;
    font-weight: 600;
    font-size: 21px;
    line-height: 26px;
    color: var(--ink);
  }
  .contact {
    position: absolute;
    top: 235px;
    left: 0;
    right: 0;
    font-family: "Arimo", Arial, sans-serif;
    font-size: 13.5px;
    line-height: 19px;
  }
  .contact .phone { font-weight: 700; }
  .contact .sep { margin: 0 7px; }
  .social {
    position: absolute;
    top: 296px;
    left: 0;
    right: 0;
    display: flex;
    justify-content: center;
    gap: 16px;
    font-family: "Arimo", Arial, sans-serif;
    font-size: 12px;
    line-height: 20px;
    color: var(--ink);
  }
  .social-item {
    display: flex;
    align-items: center;
    gap: 5px;
  }
  .social-ring {
    width: 18px;
    height: 18px;
    border: 1.2px solid var(--ink);
    border-radius: 50%;
  }
</style>
</head>
<body>
<main class="canvas">
  <section class="business-card">
    <div class="brand">
      <span class="brand-name">Tulips Turn Gold</span>
      <span class="brand-dot"></span>
    </div>
    <p class="tagline">Making vintage feel fresh again</p>
    <div class="contact">
      <p class="phone">Ph: 0417283956</p>
      <p class="links">info@ tulipsturngold.com.au<span class="sep">|</span>www.tulipsturngold.com.au</p>
    </div>
    <div class="social">
      <span class="social-item"><span class="social-ring"></span>pagebook</span>
      <span class="social-item"><span class="social-ring"></span>Craftlo</span>
    </div>
  </section>
</main>
</body>
</html>
```